Two (Similar) Posters - Both 11" x 17"

We are looking for two posters - both 11" x 17" (vertical orientation) - to promote two consecutive, cardiology-related events:

Poster #1) The Inaugural New York ROC Brainbuzz Competition, Cocktail Reception and Whiskey Tasting (http://hb-pvl.org/brainbuzz-and-reception)

and

Poster #2) The 89th Annual Scientific Session and 27th Annual Meeting (http://hb-pvl.org/2017annualmtg)

#1 is a cocktail party with a whiskey tasting that will also feature a gameshow-like event with the med students, and #2 is an educational conference for doctors

Target Market(s)

Healthcare providers (Please do not include stock images of medical professionals; in fact, please use caution with any stock imagery, as it most likely will not be appropriate.)

Industry/Entity Type

Education

Colors

Designer to choose colors to be used in the design.

Requirements
Must have
• Each poster design should include:
• - the 4 logos of the participating organizations (I can upload various other versions if needed) along with the "wording" that goes alongside each one (see "STD_small" image as an example)
• - name of event
• - date, time and location
• - where to register
• - where to get more information
• - some artistic flavor or detailing
• Final (raw) files in an .ai, .psd, .eps or .idml format are required upon project completion.
Nice to have
• It's not crucial that these two posters "match," but it would be nice if they at least coordinated with each other. Would be nice if the designer could stay close to our color scheme (can be found here - http://hb-pvl.org/), but this isn't crucial. Posters should be upscale, neat and professional.
Should not have
• Should not be too difficult to read. These are posters that will likely be hanging on a bulletin board in hospital staff break rooms. Should not be too cartoon-like or silly. The two should not look EXACTLY the same in case people think that they are the same poster.

```html
<!DOCTYPE html>
<html lang="en">
<head>
<meta charset="utf-8">
<title>The Inaugural New York ROC Brainbuzz Competition, Cocktail Reception and Whiskey Tasting</title>
<link rel="stylesheet" href="https://fonts.googleapis.com/css2?family=EB+Garamond:wght@400;500&display=swap">
<style>
  :root {
    --navy: #0d1d6c;
    --gold: #c9aa52;
    --gold-mid: rgba(201, 170, 82, 0.55);
    --gold-soft: rgba(214, 184, 96, 0.34);
    --paper: #ffffff;
    --band: #e6eef0;
    --link: #6eb3e8;
    --ink: #111111;
  }
  * { margin: 0; padding: 0; box-sizing: border-box; }
  html, body { width: 776px; height: 1200px; overflow: hidden; }
  body {
    background: var(--navy);
    font-family: "EB Garamond", Georgia, serif;
    color: var(--navy);
    position: relative;
  }
  .poster-frame {
    position: absolute;
    left: 55px; top: 55px;
    width: 666px; height: 1090px;
    border: 14px solid var(--gold);
    background: var(--paper);
    overflow: hidden;
  }
  .crest-glow {
    position: absolute;
    left: 0; top: 0;
    width: 100%; height: 360px;
    background: radial-gradient(ellipse 62% 80% at 50% 28%, var(--gold-soft) 0%, rgba(214,184,96,0.14) 55%, rgba(255,255,255,0) 82%);
  }
  .crest-glass {
    position: absolute;
    left: 271px; top: 55px;
    width: 116px; height: 136px;
    border-radius: 4px 4px 14px 14px;
    background: linear-gradient(180deg, rgba(201,170,82,0.35) 0%, var(--gold-mid) 100%);
  }
  .crest-flourish {
    position: absolute;
    top: 83px;
    width: 174px; height: 68px;
    border-radius: 34px;
    background: var(--gold-mid);
  }
  .crest-flourish--left { left: 71px; }
  .crest-flourish--right { left: 411px; }
  .event-title {
    position: absolute;
    left: 0; top: 212px; width: 100%;
    text-align: center;
    font-weight: 400;
    font-size: 43px;
    line-height: 55px;
    letter-spacing: -0.2px;
  }
  .rule {
    position: absolute;
    left: 42px; width: 554px;
    height: 2px;
    background: var(--gold);
  }
  .rule--upper { top: 416px; }
  .rule--lower { top: 631px; }
  .when {
    position: absolute;
    left: 0; top: 438px; width: 100%;
    text-align: center;
    font-size: 32px;
    line-height: 40px;
  }
  .where {
    position: absolute;
    left: 0; top: 526px; width: 100%;
    text-align: center;
    font-size: 21px;
    line-height: 29px;
  }
  .fees {
    position: absolute;
    left: 0; top: 662px; width: 100%;
    text-align: center;
    font-size: 22px;
    line-height: 28.5px;
  }
  .register {
    position: absolute;
    left: 0; top: 768px; width: 100%;
    text-align: center;
    font-size: 22px;
  }
  .register a { color: var(--link); }
  .partners-band {
    position: absolute;
    left: 0; top: 825px;
    width: 100%; height: 265px;
    background: var(--band);
  }
  .partners { list-style: none; }
  .partner {
    position: absolute;
    top: 40px;
    width: 120px;
    display: flex;
    flex-direction: column;
    align-items: center;
    text-align: center;
    font-size: 13px;
    line-height: 15px;
    color: var(--navy);
  }
  .partner:nth-child(1) { left: 72px; }
  .partner:nth-child(2) { left: 194px; }
  .partner:nth-child(3) { left: 325px; }
  .partner:nth-child(4) { left: 452px; }
  .partner-dot {
    width: 56px; height: 56px;
    border-radius: 50%;
    background: var(--navy);
    margin-bottom: 8px;
  }
  .contact {
    position: absolute;
    left: 0; top: 154px; width: 100%;
    text-align: center;
    font-size: 14px;
    line-height: 20px;
    color: var(--ink);
  }
</style>
</head>
<body>
  <main class="poster-frame">
    <div class="crest-glow" role="img" aria-label="Gold sunburst rays radiating from behind the whiskey glass"></div>
    <div class="crest-flourish crest-flourish--left" role="img" aria-label="Gold scrollwork flourish"></div>
    <div class="crest-glass" role="img" aria-label="Gold line drawing of a whiskey tumbler"></div>
    <div class="crest-flourish crest-flourish--right" role="img" aria-label="Gold scrollwork flourish"></div>

    <h1 class="event-title">The Inaugural New York ROC<br>Brainbuzz Competition, Cocktail<br>Reception &amp; Whiskey Tasting</h1>

    <div class="rule rule--upper"></div>

    <p class="when">Wednesday, Dec. 6th, 2017<br>6:30 P.M. - 10:30 P.M.</p>

    <p class="where">Location:<br>Oak &amp; Ember, 14 E 41st St<br>New York, NY 10017</p>

    <div class="rule rule--lower"></div>

    <p class="fees">Entrance fee:<br>HBPVL/PCC Members: Free<br>Nonmembers and guests: $30</p>

    <p class="register">Register online at <a href="http://hb-pvl.org/2017annualmtg">hb-pvl.org/2017annualmtg</a></p>

    <section class="partners-band">
      <ul class="partners">
        <li class="partner"><span class="partner-dot"></span>Hudson Heart Center</li>
        <li class="partner"><span class="partner-dot"></span>Pavilion College of Cardiology</li>
        <li class="partner"><span class="partner-dot"></span>Harbor Chapter Exchange</li>
        <li class="partner"><span class="partner-dot"></span>Harbor Cardiological Society</li>
      </ul>
      <p class="contact">For more information or to inquire about becoming an<br>exhibitor, call (212) 555-0147 or email ask@hb-pvl.org</p>
    </section>
  </main>
</body>
</html>
```